business card deign

Logo needs the following on it.
1. attached logo
2. Tagline - "From cooler to cabana, we keep every gathering chilled!"
3. Name- Delia Fenwick, Founder and CPO
4. Address - 418 E. Harlow Avenue, Ste 2204, Tampa, FL. 33719
5. Phone - 720.555.0187

```html
<!DOCTYPE html>
<html lang="en">
<head>
<meta charset="UTF-8">
<title>Brimwell Business Card</title>
<link href="https://fonts.googleapis.com/css2?family=Lato:wght@400;700;900&display=swap" rel="stylesheet">
<style>
  :root {
    --stage: #d9d9d9;
    --card-dark: #1c1c1c;
    --card-dark-edge: #2e2e2e;
    --card-light: #f4f4f4;
    --ink: #111111;
    --ink-soft: #6d6d6d;
    --rule: #c8c8c8;
    --ghost: #ececec;
    --paper: #ffffff;
  }
  * { box-sizing: border-box; margin: 0; padding: 0; }
  html, body {
    width: 1200px; height: 900px; overflow: hidden;
    background: var(--stage);
    font-family: "Lato", Arial, sans-serif;
  }
  .stage {
    position: relative; width: 1200px; height: 900px;
    display: flex; flex-direction: column; align-items: center; justify-content: center; gap: 48px;
  }
  .card {
    position: relative; width: 630px; height: 360px;
    border-radius: 0 40px 0 40px; overflow: hidden;
    box-shadow: 0 10px 24px rgba(0,0,0,0.25);
  }
  .card-back {
    background: linear-gradient(160deg, var(--card-dark-edge), var(--card-dark) 60%);
    display: flex; align-items: center; justify-content: center;
  }
  .brand {
    display: flex; flex-direction: column; align-items: center; gap: 14px;
  }
  .brand-mark { width: 40px; height: 40px; border-radius: 50%; }
  .brand-name { font-weight: 900; font-size: 34px; letter-spacing: 10px; padding-left: 10px; }
  .card-back .brand-mark { background: var(--paper); }
  .card-back .brand-name { color: var(--paper); }

  .card-front { background: linear-gradient(135deg, var(--paper), var(--card-light)); }
  .ghost-shape {
    position: absolute; left: 170px; top: 110px;
    width: 230px; height: 230px; border-radius: 50%;
    background: var(--ghost);
  }
  .contact { position: absolute; left: 48px; top: 56px; z-index: 1; }
  .person-name { font-weight: 900; font-size: 22px; color: var(--ink); letter-spacing: 0.5px; }
  .person-title { font-size: 15px; color: var(--ink-soft); margin-top: 2px; }
  .details { list-style: none; margin-top: 24px; }
  .details li {
    display: flex; align-items: center; gap: 8px; white-space: nowrap;
    font-size: 14px; color: var(--ink-soft); margin-bottom: 8px;
  }
  .details svg { width: 14px; height: 14px; fill: var(--ink-soft); flex: none; }
  .rule {
    position: absolute; left: 48px; top: 236px; width: 430px; height: 1px;
    background: var(--rule); z-index: 1;
  }
  .tagline {
    position: absolute; left: 48px; top: 250px; z-index: 1; white-space: nowrap;
    font-size: 16px; color: var(--ink); letter-spacing: 0.3px;
  }
  .card-front .brand { position: absolute; right: 40px; top: 56px; }
  .card-front .brand-mark { background: var(--ink); }
  .card-front .brand-name { color: var(--ink); font-size: 26px; letter-spacing: 7px; padding-left: 7px; }
</style>
</head>
<body>
<main class="stage">
  <section class="card card-back" aria-label="Card back">
    <div class="brand">
      <span class="brand-mark"></span>
      <span class="brand-name">BRIMWELL</span>
    </div>
  </section>

  <section class="card card-front" aria-label="Card front">
    <div class="ghost-shape" role="img" aria-label="Faint brand decoration"></div>
    <div class="contact">
      <h1 class="person-name">DELIA FENWICK</h1>
      <p class="person-title">Founder and CPO</p>
      <ul class="details">
        <li>
          <svg viewBox="0 0 24 24" aria-hidden="true"><path d="M6.6 10.8a15.1 15.1 0 0 0 6.6 6.6l2.2-2.2a1 1 0 0 1 1-.25 11.4 11.4 0 0 0 3.6.57 1 1 0 0 1 1 1V20a1 1 0 0 1-1 1A17 17 0 0 1 3 4a1 1 0 0 1 1-1h3.5a1 1 0 0 1 1 1c0 1.25.2 2.45.57 3.57a1 1 0 0 1-.25 1z"/></svg>
          720.555.0187
        </li>
        <li>
          <svg viewBox="0 0 24 24" aria-hidden="true"><path d="M12 2a7 7 0 0 0-7 7c0 5.25 7 13 7 13s7-7.75 7-13a7 7 0 0 0-7-7zm0 9.5A2.5 2.5 0 1 1 12 6.5a2.5 2.5 0 0 1 0 5z"/></svg>
          418 E. Harlow Avenue, Ste 2204, Tampa, FL. 33719
        </li>
      </ul>
    </div>
    <div class="rule"></div>
    <p class="tagline">From cooler to cabana, we keep every gathering chilled!</p>
    <div class="brand">
      <span class="brand-mark"></span>
      <span class="brand-name">BRIMWELL</span>
    </div>
  </section>
</main>
</body>
</html>
```